Business Card Design Project

We need a business card to reflect the design of our website - just so it all ties in - it has a retro feel and can be found at http://www.velorasoulpair.com
We will need our phone 0437 215 964
Web address, and email velorapair@fernmail.com included
Our catch cry is "Classic Cocktail Music"
Perfect Live Music for Private & Corporate Events, Weddings and Dinner Music
Our names should be included :-
Maribel Thorne / piano & Dennis Holloway / bass
I am now also including our logo so that it can be included (in part or whole) somehow in the design
My partner thinks we should include our logo in some form in the design of the card - i will attach this here for you. I will attach eps but if you prefer another format please let me know
Regards
Mari

```html
<!DOCTYPE html>
<html lang="en">
<head>
<meta charset="utf-8">
<title>Velora – Business Card</title>
<link rel="stylesheet" href="https://fonts.googleapis.com/css2?family=Josefin+Sans:wght@300;400&display=swap">
<style>
  :root {
    --teal: #66a3a1;
    --teal-deep: #5a9593;
    --stitch: #efe3bd;
    --ink: #34373a;
    --ink-soft: #55595c;
    --paper: #f7f7f7;
    --mist: #dcdee0;
    --backdrop: #ecebe8;
  }
  * { margin: 0; padding: 0; box-sizing: border-box; }
  html, body { width: 1200px; height: 422px; overflow: hidden; }
  body {
    background: var(--backdrop);
    font-family: "Josefin Sans", sans-serif;
    color: var(--ink);
    display: flex;
    gap: 40px;
    align-items: center;
    justify-content: center;
  }
  .card {
    position: relative;
    width: 560px;
    height: 316px;
    overflow: hidden;
    box-shadow: 0 2px 8px rgba(0,0,0,.15);
  }

  /* Front */
  .card--front { background: var(--mist); }
  .front__band {
    position: absolute; left: 0; top: 0; width: 100%; height: 128px;
    background: var(--teal);
  }
  .stitch {
    position: absolute; left: 0; width: 100%;
    border-top: 1.5px dashed var(--stitch);
  }
  .front__band .stitch--top { top: 14px; }
  .front__band .stitch--bottom { top: 118px; }
  .front__pattern {
    position: absolute; left: 0; top: 128px; width: 100%; height: 188px;
    background: linear-gradient(180deg, #e3e4e6, #d6d8da);
  }
  .brand-mark {
    position: absolute; left: 56px; top: 72px;
    width: 112px; height: 112px; border-radius: 50%;
    background: var(--ink);
    display: flex; align-items: center; justify-content: center;
    color: var(--stitch);
    font-size: 22px; font-weight: 400; letter-spacing: 1px;
  }
  .tagline-main {
    position: absolute; left: 0; right: 0; bottom: 22px;
    text-align: center;
    font-size: 41px; font-weight: 400; letter-spacing: 1px;
    text-transform: uppercase;
    color: var(--ink);
  }

  /* Back */
  .card--back { background: var(--paper); }
  .back__band {
    position: absolute; left: 0; top: 186px; width: 100%; height: 130px;
    background: var(--teal);
  }
  .back__band .stitch--top { top: 6px; }
  .back__band .stitch--bottom { top: 114px; }
  .instrument-disc {
    position: absolute; left: 372px; top: 128px;
    width: 118px; height: 118px; border-radius: 50%;
    background: var(--teal);
  }
  .instrument-art {
    position: absolute; left: 360px; top: 150px;
    width: 124px; height: 56px;
    border-radius: 28px 18px 18px 28px;
    background: linear-gradient(90deg, #3d4245, #2f3336);
  }
  .duo-names {
    position: absolute; left: 18px; top: 24px;
    font-size: 22px; font-weight: 300; color: var(--ink-soft);
  }
  .contact {
    position: absolute; left: 18px; top: 60px;
    font-size: 9px; font-weight: 300; line-height: 12px; color: var(--ink-soft);
    font-style: normal;
  }
  .contact .gap { height: 12px; }
  .services {
    position: absolute; left: 18px; right: 18px; top: 288px;
    font-size: 10.5px; font-weight: 300; letter-spacing: .2px;
    text-transform: uppercase; color: var(--ink);
  }
</style>
</head>
<body>

  <section class="card card--front">
    <div class="front__band">
      <span class="stitch stitch--top"></span>
      <span class="stitch stitch--bottom"></span>
    </div>
    <div class="front__pattern" role="img" aria-label="Faint repeating monogram pattern in soft grey"></div>
    <div class="brand-mark">Velora</div>
    <p class="tagline-main">Classic Cocktail Music</p>
  </section>

  <section class="card card--back">
    <h1 class="duo-names">Maribel Thorne/Piano &amp; Dennis Holloway/Bass</h1>
    <address class="contact">
      12/48 Larkspur Lane<br>
      Wattle Bay QLD<br>
      4172 Australia
      <div class="gap"></div>
      P: 0437 215 964<br>
      E: velorapair@fernmail.com<br>
      W: http://www.velorasoulpair.com
    </address>
    <div class="back__band">
      <span class="stitch stitch--top"></span>
      <span class="stitch stitch--bottom"></span>
    </div>
    <div class="instrument-disc"></div>
    <div class="instrument-art" role="img" aria-label="Illustration of a double bass with piano keys along its body"></div>
    <p class="services">Perfect live music for private &amp; corporate events, weddings and dinner music</p>
  </section>

</body>
</html>
```